Attorney Business Card

I need a business card that looks professional yet modern. I am an Attorney. , I need a professional yet modern business card for my law practice. My logo and information have been uploaded. , I need a business card that looks professional yet modern. I am an Attorney. , I need a professional yet modern business card for my law practice. My logo and information have been uploaded.

Industry/Entity Type

Business

Requirements
Must have
• My logo which has been uploaded , my logo , My logo which has been uploaded , my logo

```html
<!DOCTYPE html>
<html lang="en">
<head>
<meta charset="utf-8">
<title>Marlowe Law Firm – Business Card</title>
<link href="https://fonts.googleapis.com/css2?family=Cinzel:wght@500&family=Open+Sans:wght@400;600&display=swap" rel="stylesheet">
<style>
  :root {
    --backdrop: #3a3a3c;
    --gold: #cfa83a;
    --gold-light: #dcb94e;
    --gold-dark: #b8922c;
    --accent-blue: #1fa6d8;
    --panel: #2b2a30;
    --ink: #1c1c1c;
    --white: #f4f4f4;
  }
  * { margin: 0; padding: 0; box-sizing: border-box; }
  html, body {
    width: 1200px; height: 801px; overflow: hidden;
    background: var(--backdrop);
  }
  .stage { position: relative; width: 1200px; height: 801px; }
  .card {
    position: absolute; top: 250px;
    width: 520px; height: 300px;
    background: linear-gradient(135deg, var(--gold-light), var(--gold) 50%, var(--gold-dark));
    box-shadow: 0 10px 30px rgba(0,0,0,.35);
  }
  .card--back { left: 50px; }
  .card--front { left: 630px; }

  /* back: contact side */
  .mini-brand {
    position: absolute; left: 22px; top: 22px;
    display: flex; align-items: center; gap: 8px;
    font-family: "Cinzel", serif; font-weight: 500; font-size: 14px;
    color: var(--accent-blue); letter-spacing: 1px;
  }
  .brand-dot {
    width: 34px; height: 34px; border-radius: 50%;
    border: 2px solid var(--accent-blue);
  }
  .contact-panel {
    position: absolute; left: 190px; top: 52px; right: 22px; height: 172px;
    background: var(--panel); border-radius: 22px;
    padding: 14px 20px;
  }
  .person-name {
    font-family: "Cinzel", serif; font-weight: 500; font-size: 19px;
    color: var(--accent-blue); letter-spacing: .5px;
  }
  .person-title {
    font-family: "Open Sans", sans-serif; font-size: 12.5px; color: var(--white);
  }
  .phone-list {
    position: absolute; right: 20px; bottom: 14px;
    font-family: "Open Sans", sans-serif; font-size: 14px; line-height: 1.3;
    color: var(--white); text-align: right; list-style: none;
  }
  .rule {
    position: absolute; left: 20px; right: 20px; height: 1px;
    background: rgba(0,0,0,.55);
  }
  .rule--top { top: 236px; }
  .rule--bottom { top: 262px; }
  .web-line {
    position: absolute; right: 22px; top: 240px;
    font-family: "Open Sans", sans-serif; font-size: 13px; color: var(--ink);
  }
  .address {
    position: absolute; left: 22px; top: 269px;
    font-family: "Open Sans", sans-serif; font-size: 13px; color: var(--ink);
    text-transform: uppercase;
  }

  /* front: brand side */
  .brand-block {
    position: absolute; inset: 0;
    display: flex; flex-direction: column; align-items: center; justify-content: center;
    gap: 6px; color: var(--accent-blue);
    font-family: "Cinzel", serif; font-weight: 500;
  }
  .brand-block .brand-dot { width: 62px; height: 62px; border-width: 3px; margin-bottom: 4px; }
  .brand-name { font-size: 46px; letter-spacing: 2px; line-height: 1; }
  .brand-sub {
    display: flex; align-items: center; gap: 12px;
    font-size: 15px; letter-spacing: 3px;
  }
  .brand-sub::before, .brand-sub::after {
    content: ""; width: 70px; height: 1px; background: var(--accent-blue);
  }
</style>
</head>
<body>
<main class="stage">
  <section class="card card--back">
    <div class="mini-brand"><span class="brand-dot"></span>Marlowe</div>
    <div class="contact-panel">
      <h1 class="person-name">DANIEL MARLOWE, ESQ.</h1>
      <p class="person-title">Attorney At LAW</p>
      <ul class="phone-list">
        <li>TEL : 213.555.0142</li>
        <li>FAX : 213.555.0187</li>
        <li>MOB : 213.555.0163</li>
      </ul>
    </div>
    <div class="rule rule--top"></div>
    <p class="web-line">daniel@marlowelaw.com / www.marlowelaw.com</p>
    <div class="rule rule--bottom"></div>
    <p class="address">4820 Harbor View Dr, Suite 900, Long Beach, CA 90802</p>
  </section>

  <section class="card card--front">
    <div class="brand-block">
      <span class="brand-dot"></span>
      <span class="brand-name">MARLOWE</span>
      <span class="brand-sub">LAW FIRM</span>
    </div>
  </section>
</main>
</body>
</html>
```